Brisket inc
keeping you above the gravel
Creative Brief
Use same font as used in my logo
Dominic Varga
47215 Harwell Ct Union City CA 94587
varga.d52@mailbox-example.net
Just the logo and tag line of the front of the business card. I have listed what I want on the back of the business card.
Dominic Varga (408) 555-0147 DomVarga@brisketgarage.com Learn more at brisketgarage.com

```html
<!DOCTYPE html>
<html lang="en">
<head>
<meta charset="utf-8">
<title>Brisket inc – Business Card</title>
<link href="https://fonts.googleapis.com/css2?family=Quicksand:wght@500;700&display=swap" rel="stylesheet">
<style>
  :root {
    --backdrop: #ece9e4;
    --card-blue: #2a789e;
    --card-white: #ffffff;
    --band-teal: #52c3cb;
    --bar-teal: #2a8fa6;
    --ink-navy: #1f3f5c;
    --ink-teal: #2a8fa6;
    --ink-dark: #14323f;
    --white: #ffffff;
  }
  * { box-sizing: border-box; margin: 0; padding: 0; }
  html, body {
    width: 1200px; height: 799px; overflow: hidden;
    background: var(--backdrop);
    font-family: "Quicksand", sans-serif;
  }
  .card {
    position: absolute; top: 264px;
    width: 470px; height: 274px;
    border-radius: 20px; overflow: hidden;
    box-shadow: 0 3px 10px rgba(0,0,0,0.18);
  }
  .card--front { left: 100px; background: var(--card-blue); }
  .card--back { left: 630px; background: var(--card-white); }

  .brand {
    position: absolute; left: 0; right: 0;
    display: flex; flex-direction: column; align-items: center;
  }
  .card--front .brand { top: 86px; }
  .card--back .brand { top: 30px; }
  .brand__name {
    display: flex; align-items: center; gap: 10px;
    font-weight: 700; font-size: 50px; line-height: 1; letter-spacing: 0.5px;
  }
  .brand__mark { width: 14px; height: 14px; }
  .card--front .brand__name { color: var(--white); }
  .card--front .brand__mark { background: var(--white); }
  .card--back .brand__name { color: var(--ink-navy); font-size: 44px; }
  .card--back .brand__mark { background: var(--ink-navy); }
  .brand__tagline {
    margin-top: 10px; font-weight: 500; font-size: 16px; letter-spacing: 0.6px;
    white-space: nowrap;
  }
  .card--front .brand__tagline { color: var(--white); }
  .card--back .brand__tagline { color: var(--ink-teal); font-size: 14px; margin-top: 12px; }

  .contact-band {
    position: absolute; left: 0; right: 0; bottom: 0; height: 126px;
    background: var(--band-teal);
  }
  .contact-band__name {
    position: absolute; top: 8px; left: 128px; width: 214px; height: 32px;
    background: var(--bar-teal); color: var(--white);
    font-weight: 700; font-size: 20px; line-height: 32px; text-align: center;
    letter-spacing: 0.5px; white-space: nowrap;
  }
  .contact-band__details {
    position: absolute; top: 50px; left: 0; right: 0;
    text-align: center; color: var(--ink-dark);
    font-weight: 500; font-size: 15px; line-height: 21px; letter-spacing: 0.3px;
    list-style: none; white-space: nowrap;
  }
</style>
</head>
<body>
  <section class="card card--front" aria-label="Business card front">
    <div class="brand">
      <div class="brand__name"><span class="brand__mark"></span>Brisket inc</div>
      <p class="brand__tagline">keeping you above the gravel</p>
    </div>
  </section>

  <section class="card card--back" aria-label="Business card back">
    <div class="brand">
      <div class="brand__name"><span class="brand__mark"></span>Brisket inc</div>
      <p class="brand__tagline">keeping you above the gravel</p>
    </div>
    <div class="contact-band">
      <p class="contact-band__name">Dominic Varga</p>
      <ul class="contact-band__details">
        <li>(408) 555-0147</li>
        <li>DomVarga@brisketgarage.com</li>
        <li>www.brisketgarage.com</li>
      </ul>
    </div>
  </section>
</body>
</html>
```